Online plant nursery needs3 seperate slides for a intro web site slide slide show

We need 3 slide graphics / banners measurments should be 960wide 540 tall and 2mb or smaller. We are an online mail order nursery that focuses sales on Peonies.
Slide 1: Use faded out photos of Peony Garden with many flowers just budding. Our logo and the Words "A Lost Spring is Never Found Again". try to use our logo in a small small watermark on all slides.
Slide 2: Use your own creativity for the slide.... message should say "Free Shipping"
Slide 3: Use your own creativity for the slide .... messgae "Shop Our Other Items". To see site it will be used on go to http://k4817395.bwterxplcuha.trial52.shopvendra.com/

Target Market(s)

home owners age 30 - 65.

Industry/Entity Type

Nursery

Requirements
Must have
• must transition well.
Should not have
• can not be larger than 2MB per file

```html
<!DOCTYPE html>
<html lang="en">
<head>
<meta charset="utf-8">
<title>Petalbrook Peonies – Shop Our Other Items</title>
<link href="https://fonts.googleapis.com/css2?family=Open+Sans:wght@400;600;700&family=Josefin+Sans:wght@300;400&family=Great+Vibes&display=swap" rel="stylesheet">
<style>
  :root {
    --pink: #e0478f;
    --pink-soft: #f3b3d0;
    --ink: #1f1f1f;
    --grey: #7a7a7a;
    --rule: #e3e3e3;
    --bg: #ffffff;
  }
  * { margin: 0; padding: 0; box-sizing: border-box; }
  html, body { width: 1200px; height: 1000px; overflow: hidden; background: var(--bg); }
  body { position: relative; font-family: "Open Sans", Arial, sans-serif; color: var(--ink); }

  .search-icon { position: absolute; left: 131px; top: 139px; }

  .brand { position: absolute; display: flex; align-items: center; gap: 10px; }
  .brand-mark { width: 44px; height: 44px; border-radius: 50%; background: var(--pink-soft); flex: none; }
  .brand-name { font-family: "Open Sans", Arial, sans-serif; font-weight: 400; color: var(--pink); white-space: nowrap; }
  .brand--header { left: 514px; top: 126px; }
  .brand--header .brand-name { font-size: 21px; }
  .brand--slide { left: 160px; top: 700px; }
  .brand--slide .brand-mark { width: 52px; height: 52px; }
  .brand--slide .brand-name { font-size: 21px; }

  .account-links { position: absolute; right: 122px; top: 139px; display: flex; align-items: center; gap: 14px;
    font-size: 8.5px; font-weight: 600; letter-spacing: .2px; text-transform: uppercase; }
  .account-links span { display: flex; align-items: center; gap: 4px; }
  .cart-count { color: var(--pink); font-weight: 700; }

  .main-nav { position: absolute; left: 120px; top: 184px; width: 958px; height: 42px;
    border-top: 1px solid var(--rule); border-bottom: 1px solid var(--rule);
    display: flex; justify-content: center; align-items: center; gap: 35px;
    font-size: 11px; font-weight: 700; text-transform: uppercase; }

  .slide-copy { position: absolute; left: 140px; top: 335px; width: 250px; text-align: center; }
  .slide-copy .kicker { font-family: "Josefin Sans", sans-serif; font-weight: 300; font-size: 31px;
    letter-spacing: 9px; color: var(--grey); line-height: 1; }
  .slide-copy .script { font-family: "Great Vibes", cursive; font-size: 72px; color: var(--pink);
    letter-spacing: 8px; line-height: 1; margin: 8px 0 14px; }
  .slide-copy .items { margin-top: 0; }

  .divider { position: absolute; left: 143px; top: 558px; width: 240px; height: 40px;
    border-radius: 20px; background: linear-gradient(90deg, #eeeeee, #f8dbe8, #eeeeee); }

  .slide-photo { position: absolute; left: 393px; top: 265px; width: 677px; height: 508px;
    background: radial-gradient(ellipse at 70% 40%, #b9a24a 0%, #8a7a55 30%, #6c6a64 60%, #5a5853 100%);
    -webkit-mask: radial-gradient(ellipse 54% 56% at 50% 50%, #000 88%, transparent 100%);
            mask: radial-gradient(ellipse 54% 56% at 50% 50%, #000 88%, transparent 100%); }

  .slide-dots { position: absolute; left: 574px; top: 762px; display: flex; gap: 7px; }
  .slide-dots i { width: 12px; height: 12px; border-radius: 50%; background: #f2f2f2; border: 1px solid #cfcfcf; }
  .slide-dots i.is-active { background: #9a9a9a; }
</style>
</head>
<body>
  <svg class="search-icon" width="20" height="20" viewBox="0 0 20 20" aria-label="Search">
    <circle cx="12" cy="8" r="5.5" fill="none" stroke="var(--pink)" stroke-width="2.2"/>
    <line x1="8" y1="12" x2="3" y2="17" stroke="var(--pink)" stroke-width="2.6" stroke-linecap="round"/>
  </svg>

  <div class="brand brand--header">
    <span class="brand-mark"></span>
    <span class="brand-name">Petalbrook Peonies</span>
  </div>

  <div class="account-links">
    <span>My Account</span>
    <span>
      <svg width="9" height="9" viewBox="0 0 10 10"><polygon points="5,0 6.2,3.6 10,3.7 7,6 8.1,9.7 5,7.5 1.9,9.7 3,6 0,3.7 3.8,3.6" fill="var(--pink)"/></svg>
      Wish List
    </span>
    <span>
      <svg width="11" height="10" viewBox="0 0 11 10"><rect x="0.5" y="3" width="10" height="7" rx="1" fill="var(--pink)"/><path d="M3 3V2a2.5 2 0 0 1 5 0v1" fill="none" stroke="var(--pink)" stroke-width="1.2"/></svg>
      <b class="cart-count">(0)</b>
    </span>
  </div>

  <nav class="main-nav">
    <span>Bicolor</span>
    <span>Intersectional Peonies</span>
    <span>Tree Peony</span>
    <span>Red</span>
    <span>Pink</span>
    <span>White</span>
    <span>Yellow</span>
  </nav>

  <div class="slide-copy">
    <p class="kicker">SHOP OUR</p>
    <p class="script">Other</p>
    <p class="kicker items">ITEMS</p>
  </div>

  <div class="divider" role="img" aria-label="Decorative scroll ornament with a small peony bloom"></div>

  <div class="brand brand--slide">
    <span class="brand-mark"></span>
    <span class="brand-name">Petalbrook Peonies</span>
  </div>

  <div class="slide-photo" role="img" aria-label="Photo of a zinc watering can with wildflowers beside a wicker basket of yellow daisies and a garden fork on a wooden bench"></div>

  <div class="slide-dots"><i></i><i class="is-active"></i><i></i></div>
</body>
</html>
```